Modernise Business Card

Our company has been operating for 10 years. With the start of the new decade we are looking to refresh our business card design. We manufacture a range of industrial product shipping to customers internationally. A copy of our current card, both sides, is attached. We are looking for a mature professional appearance.

```html
<!DOCTYPE html>
<html lang="en">
<head>
<meta charset="utf-8">
<title>Korvane Business Card</title>
<link rel="stylesheet" href="https://fonts.googleapis.com/css2?family=Montserrat:wght@800&family=Open+Sans:wght@400;600&display=swap">
<style>
  :root {
    --page: #e9e9e7;
    --card-white: #f7f7f7;
    --card-grey: #a7a7a7;
    --grey-mark: #858585;
    --ink: #2b2b2b;
    --brand-blue: #1b92c0;
    --bar: #333333;
  }
  * { margin: 0; padding: 0; box-sizing: border-box; }
  html, body { width: 1200px; height: 900px; overflow: hidden; }
  body {
    background: var(--page);
    font-family: "Open Sans", Arial, sans-serif;
    color: var(--ink);
    position: relative;
  }
  .card {
    position: absolute;
    left: 250px;
    width: 700px;
    height: 400px;
    overflow: hidden;
  }
  .card--back { top: 40px; background: var(--card-grey); }
  .card--front { top: 465px; background: var(--card-white); box-shadow: 0 1px 3px rgba(0,0,0,.15); }

  /* back side */
  .back-wordmark {
    position: absolute;
    left: 0; right: 0; top: 120px;
    text-align: center;
    font-family: "Montserrat", Arial, sans-serif;
    font-weight: 800;
    font-size: 92px;
    letter-spacing: 2px;
    color: var(--grey-mark);
  }
  .product-lines {
    position: absolute;
    left: 0; right: 0; top: 250px;
    display: flex;
    justify-content: center;
    gap: 36px;
    font-size: 17px;
    font-weight: 600;
    color: var(--ink);
  }

  /* front side */
  .edge-bar { position: absolute; width: 20px; background: var(--bar); }
  .edge-bar--left { left: 0; top: 80px; height: 170px; }
  .edge-bar--right { right: 0; top: 205px; height: 165px; }

  .front-wordmark {
    position: absolute;
    left: 40px; top: 150px;
    width: 300px;
    text-align: center;
    font-family: "Montserrat", Arial, sans-serif;
    font-weight: 800;
    font-size: 54px;
    color: var(--brand-blue);
  }
  .divider {
    position: absolute;
    left: 360px; top: 80px;
    width: 2px; height: 180px;
    background: var(--ink);
  }
  .contact {
    position: absolute;
    left: 382px; top: 88px;
    width: 285px;
  }
  .contact__name {
    font-family: "Montserrat", Arial, sans-serif;
    font-weight: 800;
    font-size: 30px;
    line-height: 1;
    color: var(--brand-blue);
    white-space: nowrap;
  }
  .contact__title { font-size: 17px; margin-top: 2px; }
  .contact__list { list-style: none; margin-top: 14px; font-size: 16px; }
  .contact__list li { display: flex; align-items: flex-start; gap: 8px; margin-bottom: 8px; white-space: nowrap; }
  .icon { width: 18px; height: 18px; flex: none; margin-top: 2px; }
  .phones { display: grid; grid-template-columns: 72px auto; line-height: 1.4; }
  .address {
    position: absolute;
    left: 40px; bottom: 36px;
    display: flex; align-items: center; gap: 8px;
    font-size: 14.5px;
    white-space: nowrap;
  }
</style>
</head>
<body>

<section class="card card--back" aria-label="Card back">
  <div class="back-wordmark">Korvane</div>
  <div class="product-lines">
    <span>Hydraulic Adapters</span>
    <span>Hose Fittings</span>
    <span>Quick Couplings</span>
  </div>
</section>

<section class="card card--front" aria-label="Card front">
  <div class="edge-bar edge-bar--left"></div>
  <div class="edge-bar edge-bar--right"></div>

  <div class="front-wordmark">Korvane</div>
  <div class="divider"></div>

  <div class="contact">
    <div class="contact__name">Ethan Rowley</div>
    <div class="contact__title">Managing Director</div>
    <ul class="contact__list">
      <li>
        <svg class="icon" viewBox="0 0 24 24" aria-hidden="true"><path d="M6.6 10.8a15 15 0 0 0 6.6 6.6l2.2-2.2a1 1 0 0 1 1-.25 11.4 11.4 0 0 0 3.6.57 1 1 0 0 1 1 1V20a1 1 0 0 1-1 1A17 17 0 0 1 3 4a1 1 0 0 1 1-1h3.5a1 1 0 0 1 1 1c0 1.25.2 2.45.57 3.570a1 1 0 0 1-.25 1z" fill="none" stroke="var(--brand-blue)" stroke-width="2"/></svg>
        <div class="phones">
          <span>China</span><span>+86 138 5520 0417</span>
          <span>Australia</span><span>+61 412 785 903</span>
        </div>
      </li>
      <li>
        <svg class="icon" viewBox="0 0 24 24" aria-hidden="true"><rect x="2" y="5" width="20" height="14" fill="none" stroke="var(--brand-blue)" stroke-width="2.4"/><path d="M2 5l10 8 10-8" fill="none" stroke="var(--brand-blue)" stroke-width="2.4"/></svg>
        <span>erowley@korvanefittings.com</span>
      </li>
      <li>
        <svg class="icon" viewBox="0 0 24 24" aria-hidden="true"><circle cx="12" cy="12" r="10" fill="var(--brand-blue)"/><path d="M2 12h20M12 2v20M5 6.5h14M5 17.5h14" stroke="#fff" stroke-width="1.2"/><ellipse cx="12" cy="12" rx="4.5" ry="10" fill="none" stroke="#fff" stroke-width="1.2"/></svg>
        <span>www.korvanefittings.com</span>
      </li>
    </ul>
  </div>

  <div class="address">
    <svg class="icon" viewBox="0 0 24 24" aria-hidden="true"><path d="M12 2a7 7 0 0 0-7 7c0 5 7 13 7 13s7-8 7-13a7 7 0 0 0-7-7z" fill="var(--brand-blue)"/><circle cx="12" cy="9" r="2.6" fill="#fff"/></svg>
    <span>Suite 802, Lantern Tower 117 Harbour Road, Jiangbei District Ningbo 315000 China</span>
  </div>
</section>

</body>
</html>
```